120 years jubilee KOLVER und SANDT

We are celebrating very proud our 120 years in 5 generations
see our briefing
the invitations card should look elegant, modern, colourful as we are
our motto: mirrorpicture

```html
<!DOCTYPE html>
<html lang="en">
<head>
<meta charset="utf-8">
<title>Kolver und Sandt – Mirror Picture Invitation</title>
<link href="https://fonts.googleapis.com/css2?family=Jost:ital,wght@0,300;0,400;0,500;0,600;1,600&family=Didact+Gothic&display=swap" rel="stylesheet">
<style>
  :root{
    --paper:#ffffff;
    --sand:#e9ba89;
    --sand-soft:#f3dcc2;
    --wine:#5a1e2b;
    --ink:#141414;
    --leaf:#7f9278;
    --rust:#a4493a;
    --rose:#cf8a80;
  }
  *{margin:0;padding:0;box-sizing:border-box;}
  html,body{width:920px;height:1200px;overflow:hidden;background:var(--paper);}
  .invitation{position:relative;width:920px;height:1200px;background:var(--paper);overflow:hidden;
    font-family:"Didact Gothic",sans-serif;color:var(--ink);}
  .art{position:absolute;inset:0;width:920px;height:1200px;}
  .brand{position:absolute;top:212px;left:0;width:920px;display:flex;justify-content:center;align-items:center;gap:16px;}
  .brand-dot{width:30px;height:30px;border-radius:50%;background:var(--rust);}
  .brand-name{font-family:"Jost",sans-serif;font-weight:500;font-size:42px;color:var(--wine);letter-spacing:0.5px;}
  .title{position:absolute;top:390px;left:0;width:920px;text-align:center;font-family:"Jost",sans-serif;
    font-size:84px;line-height:1;color:var(--sand);letter-spacing:1px;}
  .title .light{font-weight:300;}
  .title .bold{font-weight:600;}
  .subtitle{position:absolute;top:482px;left:0;width:920px;text-align:center;font-family:"Jost",sans-serif;
    font-weight:400;font-size:26px;}
  .tagline{position:absolute;top:518px;left:186px;width:548px;height:30px;border-radius:15px;background:var(--wine);
    color:#fff;font-family:"Jost",sans-serif;font-size:19px;line-height:30px;text-align:center;letter-spacing:0.3px;}
  .programme{position:absolute;top:601px;left:0;width:920px;text-align:center;}
  .section-label{display:inline-block;height:28px;padding:0 16px;border-radius:14px;background:var(--sand);color:#fff;
    font-family:"Jost",sans-serif;font-style:italic;font-weight:600;font-size:18px;line-height:28px;letter-spacing:0.8px;}
  .section{margin-bottom:11px;}
  .section p{font-size:16.5px;line-height:19.5px;letter-spacing:0.4px;}
  .section-label + div{margin-top:7px;}
  .event-tab{position:absolute;left:175px;top:1064px;width:571px;height:136px;background:var(--sand);
    border-radius:52px 52px 0 0;color:#fff;text-align:center;}
  .event-date{display:flex;justify-content:center;align-items:center;margin-top:26px;font-family:"Jost",sans-serif;
    font-weight:400;font-size:35px;letter-spacing:1px;}
  .event-date .divider{width:2px;height:46px;background:#fff;margin:0 14px;}
  .event-place{margin-top:17px;font-size:15px;line-height:20px;letter-spacing:0.4px;}
</style>
</head>
<body>
<main class="invitation">
  <svg class="art" viewBox="0 0 920 1200" aria-hidden="false">
    <defs>
      <radialGradient id="washTone" cx="50%" cy="50%" r="50%">
        <stop offset="80%" stop-color="#f3dcc2" stop-opacity="0"/>
        <stop offset="92%" stop-color="#e8c49c" stop-opacity="0.55"/>
        <stop offset="100%" stop-color="#f3dcc2" stop-opacity="0"/>
      </radialGradient>
      <linearGradient id="topFloralTone" x1="0" y1="0" x2="1" y2="1">
        <stop offset="0" stop-color="#e9cfae"/>
        <stop offset="0.35" stop-color="#7f9278"/>
        <stop offset="0.6" stop-color="#efe6da"/>
        <stop offset="1" stop-color="#a4493a"/>
      </linearGradient>
      <linearGradient id="bottomFloralTone" x1="0" y1="0" x2="1" y2="1">
        <stop offset="0" stop-color="#e4c39a"/>
        <stop offset="0.3" stop-color="#6b2d3a"/>
        <stop offset="0.55" stop-color="#cf8a80"/>
        <stop offset="0.8" stop-color="#d6b07e"/>
        <stop offset="1" stop-color="#6f8268"/>
      </linearGradient>
    </defs>
    <g role="img" aria-label="Soft watercolour wash framing the invitation">
      <ellipse cx="470" cy="620" rx="470" ry="620" fill="url(#washTone)"/>
    </g>
    <g role="img" aria-label="Watercolour bouquet of white blossoms, palm leaves and rust fronds">
      <path d="M500,0 L920,0 L920,345 C890,360 860,350 830,330 C790,300 760,260 720,230 C660,190 600,120 560,70 C535,40 515,20 500,0Z" fill="url(#topFloralTone)" opacity="0.9"/>
    </g>
    <g role="img" aria-label="Watercolour arrangement of pink peony, protea, dried palm and green leaves">
      <path d="M0,560 C40,560 70,620 80,700 C100,780 130,840 190,900 C260,960 330,990 420,1000 C500,1010 560,1040 600,1090 L610,1200 L0,1200Z" fill="url(#bottomFloralTone)" opacity="0.9"/>
    </g>
  </svg>

  <header class="brand">
    <span class="brand-dot"></span>
    <span class="brand-name">Kolver und Sandt</span>
  </header>

  <h1 class="title"><span class="light">MIRROR</span> <span class="bold">PICTURE</span></h1>
  <p class="subtitle">THE ART OF RECOGNITION</p>
  <p class="tagline">proud of our 5 generations in 120 years -since 1903</p>

  <section class="programme">
    <div class="section">
      <span class="section-label">DESIGNERS</span>
      <div>
        <p>Lena Marvik "today is euphoria"</p>
        <p>Jonas Brell "reflection of art"</p>
      </div>
    </div>
    <div class="section">
      <span class="section-label">LIVESHOWS</span>
      <div>
        <p>How the Viennese weave is created</p>
        <p>How the Orvin Lounge Chair is created</p>
        <p>Building Modula shelving yourself</p>
        <p>Experience 3D rooms live and in person</p>
      </div>
    </div>
    <div class="section">
      <span class="section-label">OUR SHOWROOM</span>
      <div>
        <p>A reflection of individuality + creativity</p>
      </div>
    </div>
  </section>

  <footer class="event-tab">
    <div class="event-date"><span>15 SEP 2023</span><span class="divider"></span><span>AT 7:00 PM</span></div>
    <div class="event-place">
      <p>1010 Vienna, Lindenring 22 / at Ahornplatz</p>
      <p>on the ground floor and on the 1st floor</p>
    </div>
  </footer>
</main>
</body>
</html>
```